Real Estate For Sale Sign

I need to design a for sale sign. It needs to include The following information
Logo: Attached
Name: Marta Vinson,
Company Name: Copper Hollow Real Estate,
Phone Number: 555-304-1927
BRE Licence Number 04837215 (Can Be small)
Sign size 24x30

I am not sure about including my website but I would like to see options with it. www.copperhollowhomes.example

Target Market(s)

Potential Buyers or Sellers of Real Estate. Must be easy to read.

Industry/Entity Type

Real Estate

Requirements
Must have
• I want it to feel luxurious and sharp.

```html
<!DOCTYPE html>
<html lang="en">
<head>
<meta charset="utf-8">
<title>Copper Hollow Real Estate – For Sale Sign</title>
<link rel="stylesheet" href="https://fonts.googleapis.com/css2?family=Tinos&display=swap">
<style>
  :root {
    --page-bg: #ececec;
    --sign-bg-top: #1d1d1d;
    --sign-bg-bottom: #0c0c0c;
    --brand-blue: #2f5fae;
    --text-white: #ffffff;
    --rule-grey: #8a8a8a;
  }
  html, body {
    margin: 0;
    padding: 0;
    width: 1200px;
    height: 927px;
    overflow: hidden;
    background: var(--page-bg);
  }
  .sign {
    position: absolute;
    left: 181px;
    top: 126px;
    width: 839px;
    height: 674px;
    background: radial-gradient(ellipse at 50% 20%, var(--sign-bg-top), var(--sign-bg-bottom) 75%);
    font-family: "Tinos", "Times New Roman", serif;
    color: var(--text-white);
  }
  .brand-name {
    position: absolute;
    left: 300px;
    top: 128px;
    width: 510px;
    color: var(--brand-blue);
    font-weight: 400;
    line-height: 1;
    text-align: center;
  }
  .brand-name .brand-line {
    display: block;
    font-size: 46px;
    letter-spacing: 1px;
  }
  .brand-name .brand-sub {
    display: block;
    margin-top: 10px;
    font-size: 24px;
    letter-spacing: 10px;
  }
  .agent-name {
    position: absolute;
    left: 0;
    right: 0;
    top: 333px;
    text-align: center;
    font-size: 87px;
    line-height: 1;
  }
  .agent-rule {
    position: absolute;
    left: 128px;
    width: 582px;
    top: 431px;
    height: 1px;
    background: var(--rule-grey);
  }
  .licence {
    position: absolute;
    left: 0;
    right: 0;
    top: 443px;
    text-align: center;
    font-size: 23px;
    line-height: 1;
  }
  .phone {
    position: absolute;
    left: 0;
    right: 0;
    top: 509px;
    display: flex;
    justify-content: center;
    align-items: center;
    gap: 8px;
    font-size: 60px;
    line-height: 1;
  }
  .phone-icon {
    width: 48px;
    height: 48px;
  }
  .website {
    position: absolute;
    left: 0;
    right: 0;
    top: 609px;
    text-align: center;
    font-size: 29px;
    line-height: 1;
  }
</style>
</head>
<body>
  <main class="sign">
    <div class="brand-name">
      <span class="brand-line">COPPER HOLLOW</span>
      <span class="brand-sub">REAL ESTATE</span>
    </div>

    <div class="agent-name">Marta Vinson</div>
    <div class="agent-rule"></div>
    <div class="licence">BRE Licence&nbsp; 04837215</div>

    <div class="phone">
      <svg class="phone-icon" viewBox="0 0 48 48" aria-hidden="true">
        <circle cx="24" cy="24" r="21" fill="none" stroke="var(--text-white)" stroke-width="3"/>
        <path d="M17 12c-2 1-4 3-4 6 1 9 8 16 17 17 3 0 5-2 6-4l-5-5-3 2c-3-1-6-4-7-7l2-3z" fill="none" stroke="var(--text-white)" stroke-width="2.5" stroke-linejoin="round"/>
      </svg>
      <span class="phone-number">555-304-1927</span>
    </div>

    <div class="website">www.copperhollowhomes.example</div>
  </main>
</body>
</html>
```